Business cards and logo for a international shipping company called Meridane Freight LLC. We would like to incorporate the colors red and blue. We would like the theme to be nautical.

Industry/Entity Type

Business

```html
<!DOCTYPE html>
<html lang="en">
<head>
<meta charset="UTF-8">
<title>Meridane Freight LLC – Business Cards</title>
<link href="https://fonts.googleapis.com/css2?family=Open+Sans:wght@400;600;800&display=swap" rel="stylesheet">
<style>
  :root {
    --backdrop: #3a3d42;
    --brand-red: #b50000;
    --brand-blue: #12378f;
    --ink: #1c1c1c;
    --paper: #ffffff;
  }
  * { margin: 0; padding: 0; box-sizing: border-box; }
  html, body {
    width: 1200px; height: 864px; overflow: hidden;
    background: var(--backdrop);
    font-family: "Open Sans", Arial, sans-serif;
  }
  .stage { position: relative; width: 1200px; height: 864px; }

  .card {
    position: absolute;
    width: 580px; height: 330px;
    border-radius: 3px;
    box-shadow: 0 10px 28px rgba(0,0,0,0.45);
  }

  /* Front */
  .card-front {
    left: 310px; top: 60px;
    background: var(--brand-red);
    display: flex; align-items: center; justify-content: center;
  }
  .front-wordmark {
    color: var(--paper);
    font-weight: 800;
    font-size: 52px;
    line-height: 0.95;
    text-transform: uppercase;
    letter-spacing: 0.5px;
  }

  /* Back */
  .card-back {
    left: 310px; top: 460px;
    background: var(--paper);
    color: var(--ink);
  }
  .back-logo {
    position: absolute; right: 48px; top: 52px;
    display: flex; align-items: center; gap: 12px;
  }
  .logo-dot {
    width: 22px; height: 22px; border-radius: 50%;
    background: var(--brand-red);
  }
  .logo-name {
    color: var(--brand-blue);
    font-weight: 800;
    font-size: 34px;
    line-height: 0.95;
    text-transform: uppercase;
  }
  .holder { position: absolute; left: 40px; top: 142px; }
  .holder-name { font-size: 21px; font-weight: 600; line-height: 1.1; }
  .holder-name .first { color: var(--brand-red); }
  .holder-name .last { color: var(--brand-blue); }
  .holder-role { font-size: 13px; color: var(--ink); margin-top: 2px; }

  .divider {
    position: absolute; left: 190px; right: 40px; top: 190px;
    height: 2px; background: var(--brand-red);
  }

  .contact {
    position: absolute; right: 40px; top: 206px;
    list-style: none; text-align: right;
    font-size: 14px; line-height: 21px;
  }
  .contact li { display: flex; justify-content: flex-end; align-items: center; gap: 8px; }
  .contact svg { width: 11px; height: 11px; fill: var(--brand-red); }
  .address {
    position: absolute; right: 40px; top: 276px;
    font-size: 14px; color: var(--ink);
  }
</style>
</head>
<body>
<main class="stage">
  <section class="card card-front" aria-label="Card front">
    <div class="front-wordmark">Meridane<br>Freight</div>
  </section>

  <section class="card card-back" aria-label="Card back">
    <div class="back-logo">
      <span class="logo-dot"></span>
      <span class="logo-name">Meridane<br>Freight</span>
    </div>

    <div class="holder">
      <p class="holder-name"><span class="first">Elias</span> <span class="last">Varnholt</span></p>
      <p class="holder-role">Managing Director</p>
    </div>

    <div class="divider"></div>

    <ul class="contact">
      <li>041-555 208 317
        <svg viewBox="0 0 24 24" aria-hidden="true"><path d="M6.6 10.8a15.1 15.1 0 0 0 6.6 6.6l2.2-2.2a1 1 0 0 1 1-.25 11.4 11.4 0 0 0 3.6.57 1 1 0 0 1 1 1V20a1 1 0 0 1-1 1A17 17 0 0 1 3 4a1 1 0 0 1 1-1h3.5a1 1 0 0 1 1 1c0 1.25.2 2.45.57 3.57a1 1 0 0 1-.25 1z"/></svg>
      </li>
      <li>hello@meridanefreight.com
        <svg viewBox="0 0 24 24" aria-hidden="true"><path d="M2 5h20v14H2z M2 5l10 8 10-8" fill="none" stroke="#b50000" stroke-width="2.4"/></svg>
      </li>
      <li>www.meridanefreight.com
        <svg viewBox="0 0 24 24" aria-hidden="true"><path d="M10 14a5 5 0 0 0 7 0l3-3a5 5 0 0 0-7-7l-1 1M14 10a5 5 0 0 0-7 0l-3 3a5 5 0 0 0 7 7l1-1" fill="none" stroke="#b50000" stroke-width="2.4"/></svg>
      </li>
    </ul>
    <p class="address">48 Harbour Quay Road, Port Calder, Norland 60214.</p>
  </section>
</main>
</body>
</html>
```